USB Flash Drive Catalogue

I would like to make a paper catalogue of the products from our Quilvo store. There are currently 209 items on Quilvo. Some would be excluded. The listings have pricing and would need to be organized a bit different but all the information is there.

https://www.quilvo-example.com/shop/PebbleMarlow/items?ref=pagination&page=1

Store

```html
<!DOCTYPE html>
<html lang="en">
<head>
<meta charset="utf-8">
<title>PebbleMarlow Catalog – Pages 3–4</title>
<link rel="stylesheet" href="https://fonts.googleapis.com/css2?family=Ubuntu:wght@400;500;700&display=swap">
<style>
  :root {
    --orange: #d98a3a;
    --orange-dark: #c97a2c;
    --ink: #3d3d3d;
    --ink-soft: #6b6b6b;
    --rule: #bdbdbd;
    --paper: #ffffff;
    --paper-shade: #f3f3f3;
    --backdrop: #d8d7d2;
    --footer-band: #4a4a4a;
    --maple-a: #eeeae3;
    --maple-b: #cfc6b6;
    --walnut-a: #6e5140;
    --walnut-b: #3f2c22;
    --photo-a: #f0dca6;
    --photo-b: #c9a866;
  }
  * { box-sizing: border-box; margin: 0; padding: 0; }
  html, body { width: 1200px; height: 804px; overflow: hidden; }
  body {
    background: var(--backdrop);
    font-family: "Ubuntu", sans-serif;
    color: var(--ink);
    display: flex;
    align-items: center;
    justify-content: center;
  }
  .spread { display: flex; width: 1160px; height: 772px; box-shadow: 0 6px 22px rgba(0,0,0,.18); }
  .page {
    position: relative;
    width: 580px;
    height: 772px;
    background: linear-gradient(90deg, var(--paper) 0%, var(--paper) 90%, var(--paper-shade) 100%);
    display: flex;
    flex-direction: column;
  }
  .page--right { background: linear-gradient(90deg, var(--paper-shade) 0%, var(--paper) 10%, var(--paper) 100%); }

  /* Header */
  .page-header { position: relative; height: 58px; }
  .page-header svg { position: absolute; inset: 0; }
  .tagline {
    position: absolute; top: 17px;
    font-size: 10px; color: #fff; letter-spacing: .2px;
  }
  .page--left .tagline { left: 28px; }
  .page--right .tagline { right: 28px; }
  .brand {
    position: absolute; top: 16px;
    display: flex; align-items: center; gap: 6px;
    font-size: 11px; letter-spacing: 2px; color: var(--ink);
    text-transform: uppercase;
  }
  .page--left .brand { right: 30px; }
  .page--right .brand { left: 30px; }
  .brand-dot { width: 11px; height: 11px; border-radius: 50%; background: var(--ink); }

  /* Product grid */
  .products {
    flex: 1;
    display: grid;
    grid-template-columns: 1fr 1fr;
    grid-auto-flow: column;
    grid-template-rows: repeat(5, 1fr);
    column-gap: 34px;
    padding: 14px 34px 8px;
  }
  .item { display: flex; flex-direction: column; justify-content: center; }
  .thumb { width: 66px; height: 46px; margin-left: 20px; border-radius: 3px; margin-bottom: 4px; }
  .thumb--maple { background: linear-gradient(135deg, var(--maple-a), var(--maple-b)); }
  .thumb--walnut { background: linear-gradient(135deg, var(--walnut-a), var(--walnut-b)); }
  .thumb--photo { background: linear-gradient(135deg, var(--photo-a), var(--photo-b)); }
  .item-head {
    display: flex; justify-content: space-between; align-items: flex-end;
    border-bottom: 1.5px solid var(--orange);
    padding-bottom: 2px;
  }
  .item-name { font-size: 12.5px; font-weight: 500; color: var(--ink); }
  .tag { display: flex; flex-direction: column; align-items: flex-end; margin-bottom: -10px; }
  .cap { font-size: 11px; font-weight: 500; color: var(--orange); line-height: 1.1; }
  .price {
    background: var(--orange); color: #fff;
    font-size: 12px; font-weight: 500;
    padding: 2px 5px; line-height: 1.2;
  }
  .spec { font-size: 6.6px; line-height: 1.35; color: var(--ink-soft); margin-top: 3px; padding-right: 56px; }
  .spec b { color: var(--ink); font-weight: 500; }
  .spec .dim { padding-left: 10px; }
  .blurb { font-size: 7px; color: var(--ink-soft); margin-top: 4px; }
  .overall { font-size: 6.6px; color: var(--ink-soft); margin-top: 5px; line-height: 1.35; }
  .overall b { color: var(--ink); font-weight: 500; }

  /* Footer */
  .page-footer { display: flex; height: 34px; align-items: stretch; }
  .footer-label {
    width: 150px; background: var(--orange); color: #fff;
    font-size: 10px; display: flex; align-items: center; justify-content: center;
  }
  .footer-band {
    flex: 1; background: var(--footer-band); color: #e6e6e6;
    font-size: 7.5px; display: flex; align-items: center; justify-content: center;
    position: relative; border-left: 4px solid #8d8d8d;
  }
  .page--right .footer-band { border-left: 0; border-right: 4px solid #8d8d8d; }
  .page-number {
    position: absolute; top: 7px;
    width: 20px; height: 20px; border-radius: 50%;
    background: var(--orange); border: 2px solid #fff; color: #fff;
    font-size: 9px; font-weight: 700;
    display: flex; align-items: center; justify-content: center;
  }
  .page--left .page-number { right: 14px; }
  .page--right .page-number { left: 14px; }
</style>
</head>
<body>
<main class="spread">

  <!-- Page 3 -->
  <section class="page page--left">
    <header class="page-header">
      <svg width="580" height="58" viewBox="0 0 580 58" aria-hidden="true">
        <polygon points="0,0 270,0 300,38 0,38" fill="var(--orange)"/>
        <line x1="0" y1="44" x2="580" y2="44" stroke="var(--rule)" stroke-width="3"/>
      </svg>
      <p class="tagline">USA Company Based in Larchmont Falls, MN</p>
      <div class="brand"><span class="brand-dot"></span>PebbleMarlow</div>
    </header>

    <div class="products">
      <article class="item">
        <div class="thumb thumb--maple" role="img" aria-label="Engraved maple gift box with USB drive"></div>
        <div class="item-head"><h3 class="item-name">Antique Maple Wood</h3><div class="tag"><span class="cap">16 GB</span><span class="price">$ 25.95</span></div></div>
        <p class="spec"><b>(1) Laser Engraved Maple wooden box filled Raffia grass.</b><br><span class="dim">Approximate dimensions: 104 x 96 x 39mm</span><br><b>(1) 16GB maple wood USB drive, Wildwood Body, painted in Wedding White.</b><br><span class="dim">Approximate dimensions: 60 x 28 x 10mm</span></p>
      </article>
      <article class="item">
        <div class="thumb thumb--walnut" role="img" aria-label="Walnut wood flash drive in box"></div>
        <div class="item-head"><h3 class="item-name">Walnut Wood Flash Drive</h3><div class="tag"><span class="cap">8GB/16GB</span><span class="price">$ 22.95</span></div></div>
        <p class="blurb">Great for artisans, enthusiasts, and gift givers!</p>
        <p class="overall"><b>Over all dimensions:</b><br>180x130x60mm</p>
      </article>
      <article class="item">
        <div class="thumb thumb--maple" role="img" aria-label="Engraved maple gift box with USB drive"></div>
        <div class="item-head"><h3 class="item-name">Antique Maple Wood</h3><div class="tag"><span class="cap">16 GB</span><span class="price">$ 25.95</span></div></div>
        <p class="spec"><b>(1) Laser Engraved Maple wooden box filled Raffia grass.</b><br><span class="dim">Approximate dimensions: 104 x 96 x 39mm</span><br><b>(1) 16GB maple wood USB drive, Wildwood Body, painted in Wedding White.</b><br><span class="dim">Approximate dimensions: 60 x 28 x 10mm</span></p>
      </article>
      <article class="item">
        <div class="thumb thumb--maple" role="img" aria-label="Engraved maple gift box with USB drive"></div>
        <div class="item-head"><h3 class="item-name">Antique Maple Wood</h3><div class="tag"><span class="cap">16 GB</span><span class="price">$ 25.95</span></div></div>
        <p class="spec"><b>(1) Laser Engraved Maple wooden box filled Raffia grass.</b><br><span class="dim">Approximate dimensions: 104 x 96 x 39mm</span><br><b>(1) 16GB maple wood USB drive, Wildwood Body, painted in Wedding White.</b><br><span class="dim">Approximate dimensions: 60 x 28 x 10mm</span></p>
      </article>
      <article class="item">
        <div class="thumb thumb--walnut" role="img" aria-label="Walnut wood flash drive in box"></div>
        <div class="item-head"><h3 class="item-name">Walnut Wood Flash Drive</h3><div class="tag"><span class="cap">8GB/16GB</span><span class="price">$ 22.95</span></div></div>
        <p class="blurb">Great for artisans, enthusiasts, and gift givers!</p>
        <p class="overall"><b>Over all dimensions:</b><br>180x130x60mm</p>
      </article>

      <article class="item">
        <div class="thumb thumb--maple" role="img" aria-label="White maple box with pink heart USB drive"></div>
        <div class="item-head"><h3 class="item-name">Antique Maple Wood</h3><div class="tag"><span class="cap">16 GB</span><span class="price">$ 21.95</span></div></div>
        <p class="spec"><b>(1) Laser Engraved Maple wooden box filled Raffia grass.</b><br><span class="dim">Approximate dimensions: 104 x 96 x 39mm</span><br><b>(1) maple wood USB drive, painted in Wedding White.</b><br><span class="dim">Approximate dimensions: 60 x 28 x 10mm</span></p>
      </article>
      <article class="item">
        <div class="thumb thumb--photo" role="img" aria-label="Engraved wooden photo box"></div>
        <div class="item-head"><h3 class="item-name">Wooden Photo Box</h3><div class="tag"><span class="cap">4x6</span><span class="price">$ 22.95</span></div></div>
        <p class="blurb">Great for artisans, enthusiasts, and gift givers!</p>
        <p class="overall"><b>Over all dimensions:</b><br>180x130x60mm</p>
      </article>
      <article class="item">
        <div class="thumb thumb--maple" role="img" aria-label="White maple box with pink heart USB drive"></div>
        <div class="item-head"><h3 class="item-name">Antique Maple Wood</h3><div class="tag"><span class="cap">16 GB</span><span class="price">$ 21.95</span></div></div>
        <p class="spec"><b>(1) Laser Engraved Maple wooden box filled Raffia grass.</b><br><span class="dim">Approximate dimensions: 104 x 96 x 39mm</span><br><b>(1) maple wood USB drive, painted in Wedding White.</b><br><span class="dim">Approximate dimensions: 60 x 28 x 10mm</span></p>
      </article>
      <article class="item">
        <div class="thumb thumb--maple" role="img" aria-label="White maple box with pink heart USB drive"></div>
        <div class="item-head"><h3 class="item-name">Antique Maple Wood</h3><div class="tag"><span class="cap">16 GB</span><span class="price">$ 21.95</span></div></div>
        <p class="spec"><b>(1) Laser Engraved Maple wooden box filled Raffia grass.</b><br><span class="dim">Approximate dimensions: 104 x 96 x 39mm</span><br><b>(1) maple wood USB drive, painted in Wedding White.</b><br><span class="dim">Approximate dimensions: 60 x 28 x 10mm</span></p>
      </article>
      <article class="item">
        <div class="thumb thumb--photo" role="img" aria-label="Engraved wooden photo box"></div>
        <div class="item-head"><h3 class="item-name">Wooden Photo Box</h3><div class="tag"><span class="cap">4x6</span><span class="price">$ 22.95</span></div></div>
        <p class="blurb">Great for artisans, enthusiasts, and gift givers!</p>
        <p class="overall"><b>Over all dimensions:</b><br>180x130x60mm</p>
      </article>
    </div>

    <footer class="page-footer">
      <div class="footer-label">PebbleMarlow Catalog</div>
      <div class="footer-band">https://www.quilvo-example.com/shop/PebbleMarlow/items?ref=pagination&amp;page=1<span class="page-number">3</span></div>
    </footer>
  </section>

  <!-- Page 4 -->
  <section class="page page--right">
    <header class="page-header">
      <svg width="580" height="58" viewBox="0 0 580 58" aria-hidden="true">
        <polygon points="310,0 580,0 580,38 280,38" fill="var(--orange)"/>
        <line x1="0" y1="44" x2="580" y2="44" stroke="var(--rule)" stroke-width="3"/>
      </svg>
      <div class="brand"><span class="brand-dot"></span>PebbleMarlow</div>
      <p class="tagline">USA Company Based in Larchmont Falls, MN</p>
    </header>

    <div class="products">
      <article class="item">
        <div class="thumb thumb--maple" role="img" aria-label="Engraved maple gift box with USB drive"></div>
        <div class="item-head"><h3 class="item-name">Antique Maple Wood</h3><div class="tag"><span class="cap">16 GB</span><span class="price">$ 25.95</span></div></div>
        <p class="spec"><b>(1) Laser Engraved Maple wooden box filled Raffia grass.</b><br><span class="dim">Approximate dimensions: 104 x 96 x 39mm</span><br><b>(1) 16GB maple wood USB drive, Wildwood Body, painted in Wedding White.</b><br><span class="dim">Approximate dimensions: 60 x 28 x 10mm</span></p>
      </article>
      <article class="item">
        <div class="thumb thumb--walnut" role="img" aria-label="Walnut wood flash drive in box"></div>
        <div class="item-head"><h3 class="item-name">Walnut Wood Flash Drive</h3><div class="tag"><span class="cap">8GB/16GB</span><span class="price">$ 22.95</span></div></div>
        <p class="blurb">Great for artisans, enthusiasts, and gift givers!</p>
        <p class="overall"><b>Over all dimensions:</b><br>180x130x60mm</p>
      </article>
      <article class="item">
        <div class="thumb thumb--maple" role="img" aria-label="Engraved maple gift box with USB drive"></div>
        <div class="item-head"><h3 class="item-name">Antique Maple Wood</h3><div class="tag"><span class="cap">16 GB</span><span class="price">$ 25.95</span></div></div>
        <p class="spec"><b>(1) Laser Engraved Maple wooden box filled Raffia grass.</b><br><span class="dim">Approximate dimensions: 104 x 96 x 39mm</span><br><b>(1) 16GB maple wood USB drive, Wildwood Body, painted in Wedding White.</b><br><span class="dim">Approximate dimensions: 60 x 28 x 10mm</span></p>
      </article>
      <article class="item">
        <div class="thumb thumb--maple" role="img" aria-label="Engraved maple gift box with USB drive"></div>
        <div class="item-head"><h3 class="item-name">Antique Maple Wood</h3><div class="tag"><span class="cap">16 GB</span><span class="price">$ 25.95</span></div></div>
        <p class="spec"><b>(1) Laser Engraved Maple wooden box filled Raffia grass.</b><br><span class="dim">Approximate dimensions: 104 x 96 x 39mm</span><br><b>(1) 16GB maple wood USB drive, Wildwood Body, painted in Wedding White.</b><br><span class="dim">Approximate dimensions: 60 x 28 x 10mm</span></p>
      </article>
      <article class="item">
        <div class="thumb thumb--walnut" role="img" aria-label="Walnut wood flash drive in box"></div>
        <div class="item-head"><h3 class="item-name">Walnut Wood Flash Drive</h3><div class="tag"><span class="cap">8GB/16GB</span><span class="price">$ 22.95</span></div></div>
        <p class="blurb">Great for artisans, enthusiasts, and gift givers!</p>
        <p class="overall"><b>Over all dimensions:</b><br>180x130x60mm</p>
      </article>

      <article class="item">
        <div class="thumb thumb--maple" role="img" aria-label="White maple box with pink heart USB drive"></div>
        <div class="item-head"><h3 class="item-name">Antique Maple Wood</h3><div class="tag"><span class="cap">16 GB</span><span class="price">$ 21.95</span></div></div>
        <p class="spec"><b>(1) Laser Engraved Maple wooden box filled Raffia grass.</b><br><span class="dim">Approximate dimensions: 104 x 96 x 39mm</span><br><b>(1) maple wood USB drive, painted in Wedding White.</b><br><span class="dim">Approximate dimensions: 60 x 28 x 10mm</span></p>
      </article>
      <article class="item">
        <div class="thumb thumb--photo" role="img" aria-label="Engraved wooden photo box"></div>
        <div class="item-head"><h3 class="item-name">Wooden Photo Box</h3><div class="tag"><span class="cap">4x6</span><span class="price">$ 22.95</span></div></div>
        <p class="blurb">Great for artisans, enthusiasts, and gift givers!</p>
        <p class="overall"><b>Over all dimensions:</b><br>180x130x60mm</p>
      </article>
      <article class="item">
        <div class="thumb thumb--maple" role="img" aria-label="White maple box with pink heart USB drive"></div>
        <div class="item-head"><h3 class="item-name">Antique Maple Wood</h3><div class="tag"><span class="cap">16 GB</span><span class="price">$ 21.95</span></div></div>
        <p class="spec"><b>(1) Laser Engraved Maple wooden box filled Raffia grass.</b><br><span class="dim">Approximate dimensions: 104 x 96 x 39mm</span><br><b>(1) maple wood USB drive, painted in Wedding White.</b><br><span class="dim">Approximate dimensions: 60 x 28 x 10mm</span></p>
      </article>
      <article class="item">
        <div class="thumb thumb--maple" role="img" aria-label="White maple box with pink heart USB drive"></div>
        <div class="item-head"><h3 class="item-name">Antique Maple Wood</h3><div class="tag"><span class="cap">16 GB</span><span class="price">$ 21.95</span></div></div>
        <p class="spec"><b>(1) Laser Engraved Maple wooden box filled Raffia grass.</b><br><span class="dim">Approximate dimensions: 104 x 96 x 39mm</span><br><b>(1) maple wood USB drive, painted in Wedding White.</b><br><span class="dim">Approximate dimensions: 60 x 28 x 10mm</span></p>
      </article>
      <article class="item">
        <div class="thumb thumb--photo" role="img" aria-label="Engraved wooden photo box"></div>
        <div class="item-head"><h3 class="item-name">Wooden Photo Box</h3><div class="tag"><span class="cap">4x6</span><span class="price">$ 22.95</span></div></div>
        <p class="blurb">Great for artisans, enthusiasts, and gift givers!</p>
        <p class="overall"><b>Over all dimensions:</b><br>180x130x60mm</p>
      </article>
    </div>

    <footer class="page-footer">
      <div class="footer-band">https://www.quilvo-example.com/shop/PebbleMarlow/items?ref=pagination&amp;page=1<span class="page-number">4</span></div>
      <div class="footer-label">PebbleMarlow Catalog</div>
    </footer>
  </section>

</main>
</body>
</html>
```